Business Card Design

We have recently seen two business cards that caught our attention and think the designs would work for us. We are an accounting firm that serves small businesses in a variety of industries. Attached are the two business card that inspired us along with very rough layouts. We would like to see a professional layout using our company information.

Industry/Entity Type

Accounting

Contact Information for Business Card

Company Name - Dalworth Pryce
Address - 4180 Brambleton Lane, Suite 310, Houston, TX 77051
713-508-9627 - Main
281-369-0714 - Fax

Team Member Names, emails and phone numbers (see attachment)

```html
<!DOCTYPE html>
<html lang="en">
<head>
<meta charset="utf-8">
<title>Dalworth Pryce – Business Card</title>
<link rel="stylesheet" href="https://fonts.googleapis.com/css2?family=Cinzel:wght@600;700&family=Open+Sans:wght@400;600&display=swap">
<style>
  :root {
    --ink: #111111;
    --band: #0c0c0c;
    --grey: #6f6f6f;
    --mid: #9a9a9a;
    --paper: #ffffff;
    --stage: #e9e7e3;
    --rule: #c9c9c9;
  }
  * { box-sizing: border-box; margin: 0; padding: 0; }
  html, body { width: 1200px; height: 1023px; overflow: hidden; }
  body {
    background: var(--stage);
    display: flex; align-items: center; justify-content: center; gap: 80px;
    font-family: "Open Sans", Arial, sans-serif;
  }
  .card {
    position: relative; width: 380px; height: 640px;
    background: var(--paper);
    box-shadow: 0 10px 30px rgba(0,0,0,.18);
    overflow: hidden;
  }
  .brand {
    position: absolute; top: 70px; left: 0; right: 0;
    display: flex; flex-direction: column; align-items: center; gap: 18px;
  }
  .brand-mark { width: 70px; height: 70px; background: var(--ink); }
  .brand-name {
    font-family: "Cinzel", Georgia, serif; font-weight: 700;
    font-size: 32px; color: var(--ink); letter-spacing: 1px;
  }
  .person { position: absolute; top: 260px; left: 40px; }
  .person-name {
    font-family: "Cinzel", Georgia, serif; font-weight: 600;
    font-size: 30px; color: var(--grey); letter-spacing: 1px;
  }
  .person-title { font-size: 14px; color: var(--grey); letter-spacing: 1px; text-transform: uppercase; }
  .contacts { position: absolute; top: 350px; left: 40px; list-style: none; }
  .contacts li {
    display: flex; align-items: center; gap: 10px;
    font-size: 16px; color: var(--ink); line-height: 28px;
  }
  .contacts svg, .office svg { width: 14px; height: 14px; flex: none; }
  .rule { position: absolute; left: 0; right: 0; top: 480px; height: 2px; background: var(--rule); }
  .office {
    position: absolute; left: 0; right: 0; bottom: 0; height: 150px;
    background: linear-gradient(180deg, #2a2a2a 0%, var(--band) 40%);
    color: #e8e8e8; text-align: center; font-size: 15px; letter-spacing: .5px;
    text-transform: uppercase; padding-top: 28px; line-height: 24px;
  }
  .office-lines { display: flex; justify-content: center; align-items: center; gap: 8px; }
  .back .corner { position: absolute; top: 0; right: 0; }
  .back .brand { top: 150px; }
  .back .web {
    position: absolute; top: 400px; left: 0; right: 0; text-align: center;
    font-size: 16px; color: var(--ink); line-height: 28px;
  }
</style>
</head>
<body>
  <section class="card front">
    <div class="brand">
      <div class="brand-mark"></div>
      <div class="brand-name">Dalworth Pryce</div>
    </div>
    <div class="person">
      <div class="person-name">Maren Oakes</div>
      <div class="person-title">Account Manager</div>
    </div>
    <ul class="contacts">
      <li><svg viewBox="0 0 14 14"><rect width="14" height="14" rx="2" fill="#111"/><path d="M4 3l2 2-1 1.2c.6 1.3 1.5 2.2 2.8 2.8L9 8l2 2-1.3 1.3C6.5 11 3 7.5 2.7 4.3z" fill="#fff"/></svg>713-655-2190</li>
      <li><svg viewBox="0 0 14 14"><rect width="14" height="14" rx="2" fill="#111"/><rect x="4.5" y="2.5" width="5" height="9" rx="1" fill="#fff"/></svg>832-417-5308</li>
      <li><svg viewBox="0 0 14 14"><rect width="14" height="14" rx="2" fill="#111"/><rect x="3" y="4" width="8" height="6" fill="#fff"/><path d="M3 4l4 3 4-3" stroke="#111" fill="none"/></svg>moakes@dalworthpryce.com</li>
      <li>www.dalworthpryce.com</li>
    </ul>
    <div class="rule"></div>
    <div class="office">
      <div>4180 Brambleton Lane, Suite 310</div>
      <div>Houston, TX 77051</div>
      <div class="office-lines">
        <svg viewBox="0 0 14 14"><rect width="14" height="14" rx="2" fill="#888"/><path d="M4 3l2 2-1 1.2c.6 1.3 1.5 2.2 2.8 2.8L9 8l2 2-1.3 1.3C6.5 11 3 7.5 2.7 4.3z" fill="#111"/></svg>713-508-9627 |
        <svg viewBox="0 0 14 14"><rect width="14" height="14" rx="2" fill="#888"/><rect x="3" y="6" width="8" height="5" fill="#111"/><rect x="4.5" y="3" width="5" height="3" fill="#111"/></svg>281-369-0714
      </div>
    </div>
  </section>

  <section class="card back">
    <svg class="corner" width="200" height="200" viewBox="0 0 200 200"><polygon points="60,0 200,0 200,140" fill="#111"/></svg>
    <div class="brand">
      <div class="brand-mark"></div>
      <div class="brand-name">Dalworth Pryce</div>
    </div>
    <div class="web">
      <div>moakes@dalworthpryce.com</div>
      <div>www.dalworthpryce.com</div>
    </div>
    <div class="office">
      <div>4180 Brambleton Lane, Suite 310</div>
      <div>Houston, TX 77051</div>
      <div class="office-lines">
        <svg viewBox="0 0 14 14"><rect width="14" height="14" rx="2" fill="#888"/><path d="M4 3l2 2-1 1.2c.6 1.3 1.5 2.2 2.8 2.8L9 8l2 2-1.3 1.3C6.5 11 3 7.5 2.7 4.3z" fill="#111"/></svg>713-508-9627 |
        <svg viewBox="0 0 14 14"><rect width="14" height="14" rx="2" fill="#888"/><rect x="3" y="6" width="8" height="5" fill="#111"/><rect x="4.5" y="3" width="5" height="3" fill="#111"/></svg>281-369-0714
      </div>
    </div>
  </section>
</body>
</html>
```